Business Card & Stationery Design for a General Contracting Company
Brenwick Contracting Limited
Tolvane Perdo
Managing Director
No 7 Marlowe Crescent, Elmsby
brenwickcontracting@quillpost.net
The Company is involved in supply and transport of aggregate materials and heavy equipment rental at present. Furthermore we recently had a project for the logo design of our Company on this website and we would like to incorporate this logo into our stationery designs and business cards. Please see the links below; Our design project; http://orders.markcraftstudio.net/contests/logo-for-a-general-contracting-company The logo chosen; http://orders.markcraftstudio.net/drafts/display/contest/512093/draft/e7d4b58213690ab1c5f93d478ee2bb718204617

```html
<!DOCTYPE html>
<html lang="en">
<head>
<meta charset="utf-8">
<title>Brenwick Contracting Limited – Stationery</title>
<link href="https://fonts.googleapis.com/css2?family=Open+Sans:wght@400;600&display=swap" rel="stylesheet">
<style>
  :root{
    --bg:#e8e9eb;
    --paper:#ffffff;
    --red:#b5232a;
    --blue:#1f4e8c;
    --ink:#333a45;
    --faint:#f3e0e1;
  }
  *{box-sizing:border-box;margin:0;padding:0}
  html,body{width:1200px;height:936px;overflow:hidden}
  body{background:var(--bg);position:relative;font-family:"Open Sans",sans-serif;color:var(--ink)}
  .sheet{position:absolute;background:var(--paper);box-shadow:0 2px 6px rgba(0,0,0,.18)}
  .brand{font-family:"Open Sans",sans-serif;font-weight:600;color:var(--blue);text-align:center;line-height:1.2;display:flex;align-items:center;justify-content:center;gap:.4em}
  .brand-dot{flex:none;border-radius:50%;background:var(--red)}
  .footer-band{position:absolute;left:0;right:0;bottom:0;background:var(--red)}
  .domain-pill{position:absolute;bottom:0;background:var(--blue);color:#fff;font-size:10px;font-weight:600;display:flex;align-items:center;justify-content:center;border-radius:6px 6px 0 0}

  /* letterhead */
  .letterhead{left:177px;top:63px;width:393px;height:552px}
  .letterhead .brand{position:absolute;top:32px;left:0;right:0;font-size:13px}
  .letterhead .watermark{position:absolute;top:215px;left:0;right:0;font-size:44px;font-weight:600;color:var(--faint);text-align:center}
  .letterhead .contacts{position:absolute;left:48px;right:30px;bottom:32px;font-size:8.5px;line-height:1.6}
  .letterhead .contacts svg{width:8px;height:8px;vertical-align:-1px;margin-right:2px}
  .letterhead .footer-band{height:14px}

  /* folder */
  .folder{left:633px;top:38px;width:460px;height:577px}
  .folder .brand{position:absolute;top:250px;left:0;right:0;font-size:28px}
  .folder .footer-band{height:18px}
  .folder .domain-pill{left:140px;width:180px;height:24px}

  /* business cards */
  .card{left:43px;width:202px;height:102px}
  .card-front{top:658px}
  .card-back{top:780px}
  .card-front .brand{position:absolute;top:12px;left:12px;font-size:9px;justify-content:flex-start}
  .card-front .person{position:absolute;top:36px;left:12px;font-size:6.5px;line-height:1.4}
  .card-front .person strong{font-size:7.5px;color:var(--blue)}
  .card-front .footer-band{height:8px}
  .card-back .brand{position:absolute;top:26px;left:0;right:0;font-size:11px}
  .card-back .domain{position:absolute;bottom:10px;left:0;right:0;text-align:center;font-size:6.5px;color:var(--blue)}

  /* envelopes */
  .envelope-front{left:260px;top:658px;width:342px;height:228px}
  .envelope-front .brand{position:absolute;top:22px;left:22px;font-size:12px;justify-content:flex-start}
  .envelope-front .footer-band{height:12px}
  .envelope-front .domain-pill{left:110px;width:130px;height:18px;font-size:8px}
  .envelope-back{left:633px;top:663px;width:460px;height:223px;overflow:hidden}
  .envelope-back svg{position:absolute;left:0;top:0}
  .envelope-back .footer-band{height:12px}
  .envelope-back .domain-pill{left:150px;width:160px;height:20px;font-size:9px;border-radius:0 0 6px 6px;top:40px;bottom:auto}
</style>
</head>
<body>

<section class="sheet letterhead">
  <div class="brand"><span class="brand-dot" style="width:9px;height:9px"></span><span>Brenwick Contracting Limited</span></div>
  <div class="watermark">Brenwick</div>
  <div class="contacts">
    <svg viewBox="0 0 10 10"><circle cx="5" cy="5" r="5" fill="#1f4e8c"/></svg>No 7 Marlowe Crescent, Elmsby
    &nbsp;<svg viewBox="0 0 10 10"><circle cx="5" cy="5" r="5" fill="#1f4e8c"/></svg>555-0147
    &nbsp;<svg viewBox="0 0 10 10"><circle cx="5" cy="5" r="5" fill="#1f4e8c"/></svg>555-0183
    &nbsp;<svg viewBox="0 0 10 10"><circle cx="5" cy="5" r="5" fill="#1f4e8c"/></svg>555-0129<br>
    <svg viewBox="0 0 10 10"><circle cx="5" cy="5" r="5" fill="#1f4e8c"/></svg>brenwickcontracting@quillpost.net
    &nbsp;<svg viewBox="0 0 10 10"><circle cx="5" cy="5" r="5" fill="#1f4e8c"/></svg>www.brenwicksite.net
  </div>
  <div class="footer-band"></div>
</section>

<section class="sheet folder">
  <div class="brand"><span class="brand-dot" style="width:18px;height:18px"></span><span>Brenwick Contracting<br>Limited</span></div>
  <div class="footer-band"></div>
  <div class="domain-pill">www.brenwicksite.net</div>
</section>

<section class="sheet card card-front">
  <div class="brand">Brenwick Contracting Limited</div>
  <div class="person"><strong>Tolvane Perdo</strong><br>Managing Director<br>No 7 Marlowe Crescent, Elmsby<br>555-0147 · brenwickcontracting@quillpost.net</div>
  <div class="footer-band"></div>
</section>

<section class="sheet card card-back">
  <div class="brand"><span>Brenwick Contracting<br>Limited</span></div>
  <div class="domain">www.brenwicksite.net</div>
</section>

<section class="sheet envelope-front">
  <div class="brand">Brenwick Contracting Limited</div>
  <div class="footer-band"></div>
  <div class="domain-pill">www.brenwicksite.net</div>
</section>

<section class="sheet envelope-back">
  <svg width="460" height="223" viewBox="0 0 460 223">
    <path d="M0 0 H460 V30 Q230 110 0 30 Z" fill="#1f4e8c"/>
  </svg>
  <div class="domain-pill">www.brenwicksite.net</div>
  <div class="footer-band"></div>
</section>

</body>
</html>
```